Business card design needed for rebranded top-end landscaping business

We need a new business card design, incorporating our logo (colours Green #8dc63f and Grey #8a8c8e) and also some options that include the colour dark navy (eg #000040) as our uniforms are navy with white and grey trim.

We are an innovative landscaping company that maintains high-end gardens for meticulous clients. We pride ourselves on our customer service, our professionalism, and our workmanship.

Our business name needs to be easily read and our branding needs to be bold and memorable, without screaming "tradesman"! We prefer clean lines over lots of fine detail.

The design MUST include:
- Business name ("Brambleton Gardenworks")
- Logo (file uploaded)
- Employee name
- Phone number
- Email address
- www.brambletongardenworks.com.au
- Facebook & Instagram logos
- The Turfcraft Guild logo (file uploaded) along with the word "Member"
- Licence "Lic. 618392K"

OPTIONAL inclusions:
- "Creating outdoor spaces for our community to be inspired, refreshed and re-energised"
- "Landscape Maintenance - Irrigation - Arboriculture" (dashes can be replaced with dots or other)
- "Fully qualified, licensed & insured"
- "Residential - Strata - Commercial - Real Estate" (dashes can be replaced with dots or other)

High-end professionals and retirees, real estate agents

Landscaping

See Project description

Sans Serif

Designer to choose colors to be used in the design.

• Must incorporate our logo, and colours Green #8dc63f and Grey #8a8c8e) from the logo, and the colour DARK NAVY (eg #000040).
• The design MUST include:
• - Business name ("Brambleton Gardenworks")
• - Logo (file uploaded)
• - Employee name
• - Phone number
• - Email address
• - www.brambletongardenworks.com.au
• - Facebook & Instagram logos
• - The Turfcraft Guild logo (file uploaded) along with the word "Member"
• - Licence "Lic. 618392K"
• OPTIONAL inclusions:
• - "Creating outdoor spaces for our community to be inspired, refreshed and re-energised"
• - "Landscape Maintenance - Irrigation - Arboriculture" (dashes can be replaced with dots or other)
• - "Fully qualified, licensed & insured"
• - "Residential - Strata - Commercial - Real Estate" (dashes can be replaced with dots or other)

```html
<!DOCTYPE html>
<html lang="en">
<head>
<meta charset="utf-8">
<title>Brambleton Gardenworks – Business Card</title>
<link href="https://fonts.googleapis.com/css2?family=Montserrat:wght@400;500;600;700&display=swap" rel="stylesheet">
<style>
  :root {
    --navy: #13103c;
    --green: #8dc63f;
    --grey: #8a8c8e;
    --white: #ffffff;
    --backdrop: #e8ebe4;
  }
  * { margin: 0; padding: 0; box-sizing: border-box; }
  html, body { width: 1200px; height: 800px; overflow: hidden; }
  body {
    background: var(--backdrop);
    font-family: "Montserrat", Arial, sans-serif;
    position: relative;
  }
  .card {
    position: absolute;
    top: 236px;
    width: 540px;
    height: 328px;
    border-radius: 22px;
    overflow: hidden;
  }
  .card-front { left: 40px; background: var(--green); }
  .card-back { left: 620px; background: var(--navy); }
  .card-shape { position: absolute; inset: 0; width: 540px; height: 328px; }

  /* front */
  .brand {
    position: absolute;
    left: 110px; right: 0;
    top: 74px;
    text-align: center;
  }
  .brand-mark {
    width: 74px; height: 74px;
    margin: 0 auto 16px;
    border-radius: 50%;
    background: var(--grey);
  }
  .brand-name {
    color: var(--green);
    font-weight: 700;
    font-size: 27px;
    line-height: 1.15;
    letter-spacing: 0.2px;
  }
  .brand-services {
    margin-top: 14px;
    color: var(--grey);
    font-weight: 600;
    font-size: 10px;
    letter-spacing: 0.2px;
  }

  /* back */
  .guild {
    position: absolute;
    left: 90px; top: 50px;
    width: 82px;
    text-align: center;
  }
  .guild-badge {
    width: 30px; height: 30px;
    margin: 0 auto 10px;
    background: var(--green);
    border-radius: 4px;
  }
  .guild-member {
    color: var(--green);
    font-weight: 700;
    font-size: 11px;
    letter-spacing: 4px;
    margin-right: -4px;
  }
  .rule { position: absolute; left: 90px; width: 362px; height: 1px; }
  .rule-green { top: 127px; background: var(--green); }
  .rule-grey { top: 226px; background: var(--grey); }

  .details {
    position: absolute;
    right: 88px;
    text-align: right;
    color: var(--green);
    font-weight: 500;
  }
  .person-name { top: 102px; font-size: 16px; font-weight: 500; }
  .person-role { top: 133px; font-size: 11px; }
  .contact { top: 177px; font-size: 11px; line-height: 14px; }
  .social {
    top: 235px;
    font-size: 11px;
    display: flex;
    align-items: center;
    gap: 5px;
  }
  .social-dot { width: 14px; height: 14px; border-radius: 50%; background: var(--green); }
  .licence { top: 265px; font-size: 11px; }
</style>
</head>
<body>

  <section class="card card-front">
    <svg class="card-shape" viewBox="0 0 540 328" aria-hidden="true">
      <path d="M98 0 Q42 164 98 328 L540 328 L540 0 Z" fill="var(--navy)"/>
    </svg>
    <div class="brand">
      <div class="brand-mark"></div>
      <p class="brand-name">Brambleton<br>Gardenworks</p>
      <p class="brand-services">Landscape Maintenance • Irrigation • Arboriculture</p>
    </div>
  </section>

  <section class="card card-back">
    <svg class="card-shape" viewBox="0 0 540 328" aria-hidden="true">
      <path d="M93 0 L207 0 Q149 164 211 328 L97 328 Q47 164 93 0 Z" fill="var(--white)"/>
    </svg>
    <div class="guild">
      <div class="guild-badge"></div>
      <p class="guild-member">MEMBER</p>
    </div>
    <div class="rule rule-green"></div>
    <div class="rule rule-grey"></div>

    <p class="details person-name">Rowan Hartley</p>
    <p class="details person-role">Employee</p>
    <p class="details contact">0412 338 706<br>info@brambletongardenworks.com.au<br>www.brambletongardenworks.com.au</p>
    <div class="details social">
      <span class="social-dot"></span>
      <span class="social-dot"></span>
      <span>brambletongardenworks</span>
    </div>
    <p class="details licence">LIC. 618392K</p>
  </section>

</body>
</html>
```